Professional Consulting Firm Business Card Design

We need a business card design for a new professional consulting firm that specializes in petroleum, health, and financial consulting. We need a design that is trendy but elegant, and one that would make a summit 300 executive feel comfortable using our services. I have attached a logo that needs to be used in the design. I have also attached a photo of a card design that I like.

On the card we need a place for employee name, title, email address, fax number, phone number, mailing address, and website address.

Industry/Entity Type

Financial

Contact Information for Business Card

see attached

Other font styles liked:
• Calibri or your choice

Requirements
Must have
• style
Nice to have
• texture, rounded edges
Should not have
• no solid black cards but black may be used

```html
<!DOCTYPE html>
<html lang="en">
<head>
<meta charset="utf-8">
<title>Alder &amp; Vale Consulting – Business Cards</title>
<link href="https://fonts.googleapis.com/css2?family=Crimson+Text:wght@400;600&family=Montserrat:wght@400&display=swap" rel="stylesheet">
<style>
  :root {
    --backdrop: #2e2f31;
    --card-white: #f7f7f5;
    --navy: #0f3266;
    --navy-deep: #0a2550;
    --navy-light: #1a4580;
    --accent-blue: #2f62a3;
    --ink-grey: #5e6166;
    --on-navy: #eef2f8;
  }
  * { margin: 0; padding: 0; box-sizing: border-box; }
  html, body { width: 1200px; height: 997px; overflow: hidden; }
  body { background: var(--backdrop); position: relative; font-family: "Crimson Text", Georgia, serif; }

  .card {
    position: absolute;
    width: 560px;
    height: 320px;
    box-shadow: 0 18px 40px rgba(0,0,0,.45);
  }

  /* Front: contact side */
  .card--contact { left: 90px; top: 110px; background: var(--card-white); }
  .brand {
    position: absolute;
    display: flex;
    align-items: center;
    gap: 16px;
  }
  .brand__name {
    font-family: "Crimson Text", Georgia, serif;
    font-weight: 600;
    color: var(--accent-blue);
    white-space: nowrap;
    line-height: 1;
  }
  .brand__rule { width: 1px; background: currentColor; opacity: .6; }
  .brand__tagline {
    font-family: "Montserrat", Arial, sans-serif;
    text-transform: uppercase;
    letter-spacing: .06em;
    white-space: nowrap;
  }
  .card--contact .brand { left: 44px; top: 52px; color: var(--accent-blue); }
  .card--contact .brand__name { font-size: 30px; }
  .card--contact .brand__rule { height: 46px; }
  .card--contact .brand__tagline { font-size: 7px; color: var(--accent-blue); }

  .divider-slash {
    position: absolute; left: 360px; top: 130px;
    width: 2px; height: 56px;
    background: linear-gradient(var(--accent-blue), rgba(47,98,163,0));
    transform: rotate(-28deg);
  }
  .person { position: absolute; left: 400px; top: 118px; color: var(--accent-blue); }
  .person__name { font-weight: 600; font-size: 17px; }
  .person__title { font-size: 13px; color: var(--ink-grey); }
  .person__address { margin-top: 14px; font-size: 13px; line-height: 1.3; }

  .contact-list {
    position: absolute; left: 44px; bottom: 30px;
    list-style: none; font-size: 14px; color: var(--ink-grey);
  }
  .contact-list li { display: flex; align-items: center; gap: 10px; line-height: 1.55; }
  .contact-list svg { width: 12px; height: 12px; fill: var(--accent-blue); flex: none; }

  /* Back: brand side */
  .card--brand {
    left: 560px; top: 540px;
    background:
      linear-gradient(135deg, rgba(255,255,255,.05) 0 30%, transparent 30% 55%, rgba(0,0,0,.08) 55% 75%, transparent 75%),
      radial-gradient(ellipse at 40% 45%, var(--navy-light), var(--navy) 55%, var(--navy-deep));
  }
  .card--brand .brand {
    left: 50%; top: 50%; transform: translate(-50%, -50%);
    color: var(--on-navy);
  }
  .card--brand .brand__name { font-size: 38px; color: var(--on-navy); }
  .card--brand .brand__rule { height: 70px; }
  .card--brand .brand__tagline { font-size: 9px; color: var(--on-navy); }
</style>
</head>
<body>

<section class="card card--contact" aria-label="Business card, contact side">
  <div class="brand">
    <span class="brand__name">Alder &amp; Vale</span>
    <span class="brand__rule"></span>
    <span class="brand__tagline">Health, safety, and financial<br>consulting services</span>
  </div>

  <span class="divider-slash"></span>

  <div class="person">
    <div class="person__name">Daniel Hartwell</div>
    <div class="person__title">Chief Operating Officer</div>
    <div class="person__address">48 Alder Lane,<br>Brookfield, PA 15020</div>
  </div>

  <ul class="contact-list">
    <li>
      <svg viewBox="0 0 16 16" aria-hidden="true"><path d="M2 2h4l1.5 4-2 1.3a9 9 0 0 0 3.2 3.2L10 8.5l4 1.5v4a1 1 0 0 1-1 1C6.9 15 1 9.1 1 3a1 1 0 0 1 1-1z"/></svg>
      555-204-3180
    </li>
    <li>
      <svg viewBox="0 0 16 16" aria-hidden="true"><path d="M4 1h8v4H4zM1 6h14v6h-3v3H4v-3H1zm4 5v3h6v-3z"/></svg>
      555-204-3182
    </li>
    <li>
      <svg viewBox="0 0 16 16" aria-hidden="true"><path d="M1 3h14v10H1zm1.5 1.5L8 9l5.5-4.5z"/></svg>
      dan@aldervale.com
    </li>
    <li>
      <svg viewBox="0 0 16 16" aria-hidden="true"><path d="M6.5 9.5l3-3 1 1-3 3zM4 8l2-2 1 1-2 2a1.8 1.8 0 0 0 2.5 2.5l2-2 1 1-2 2A3.2 3.2 0 0 1 4 8zm8 0l-2 2-1-1 2-2A1.8 1.8 0 0 0 8.5 4.5l-2 2-1-1 2-2A3.2 3.2 0 0 1 12 8z"/></svg>
      www.aldervale.com
    </li>
  </ul>
</section>

<section class="card card--brand" aria-label="Business card, brand side">
  <div class="brand">
    <span class="brand__name">Alder &amp; Vale</span>
    <span class="brand__rule"></span>
    <span class="brand__tagline">Consulting<br>Health, safety, and financial consulting services</span>
  </div>
</section>

</body>
</html>
```